BriskLoom Wordpress Website

We require a WordPress website that emulates the sleek design and functionality of https://www.tulvorix.example and https://quenlap.example/. The site should showcase our AI-powered customer support solutions with a modern, professional aesthetic.
Homepage
The homepage should feature a bold headline highlighting our AI capabilities, followed by concise sections outlining our key offerings:
AI-powered customer support
Data integration and deployment
Knowledge system integration
AI help desks and chat agents
Customer feedback insights
Include eye-catching visuals or animations to illustrate these concepts.
Navigation
The main navigation menu should include:
Product
Platform
Company
News
Learn More
Key Pages
Product Page: Detail our AI solutions, their benefits, and use cases.
Platform Page: Explain our technology, integration capabilities, and deployment process.
Company Page: Share our mission, team, and values.
News Page: Feature latest updates, press releases, and blog posts.
Call-to-Action
Implement a prominent "Learn More" button that directs users to an enrollment page. Our team will manage inquiries from this point.
Footer
Include a "Contact Us" section in the footer for easy access to our contact information.
Design Elements
Use a clean, minimalist design with ample white space
Incorporate a color scheme that reflects trust and innovation
Utilize smooth scrolling and subtle animations for enhanced user experience
Ensure mobile responsiveness for all devices
Technical Requirements
Build on WordPress for easy content management
Optimize for fast loading speeds and SEO
The website should convey our expertise in AI-driven customer support solutions while providing an intuitive user experience that guides visitors toward learning more about our services
Industry/Entity Type
AI Chat Agents

```html
<!DOCTYPE html>
<html lang="en">
<head>
<meta charset="utf-8">
<title>BriskLoom — AI Chat Agents</title>
<link href="https://fonts.googleapis.com/css2?family=Lexend:wght@400;500;600&family=Inter:wght@400;500;600;700&display=swap" rel="stylesheet">
<style>
:root{
  --teal:#3f8b8f;
  --teal-dark:#2a5a62;
  --hero-a:#173f4c;
  --hero-b:#2a7479;
  --ink:#1c1f22;
  --muted:#5b6168;
  --footer:#18272b;
  --panel:#dadada;
  --white:#fff;
  --accent:#2f8f94;
}
*{box-sizing:border-box;margin:0;padding:0}
html,body{width:1200px;height:3085px;overflow:hidden}
body{position:relative;font-family:"Inter",sans-serif;color:var(--ink);background:var(--white)}
.abs{position:absolute}
h1,h2,h3,.display{font-family:"Lexend",sans-serif;font-weight:400}

/* header + hero */
.hero{left:0;top:0;width:1200px;height:666px;background:linear-gradient(160deg,var(--hero-a) 0%,#1f5a63 45%,var(--hero-b) 100%)}
.brand{display:flex;align-items:center;gap:10px;color:#fff;font-family:"Lexend",sans-serif;font-size:29px}
.brand .dot{width:46px;height:46px;border-radius:50%;background:var(--teal)}
.nav{left:535px;top:26px;display:flex;gap:43px;color:#fff;font-size:15px}
.btn{display:flex;align-items:center;justify-content:center;border-radius:30px;background:var(--teal);color:#fff;font-size:14px}
.hero-art{left:60px;top:85px;width:550px;height:525px;border-radius:30px;background:radial-gradient(circle at 50% 50%,#4a9b8a 0%,#2c6f6f 45%,rgba(30,80,90,0) 75%)}
.hero-title{left:668px;top:258px;color:#fff;font-size:56px;font-weight:600}
.hero-sub{left:670px;top:342px;width:470px;color:#e6f0f1;font-size:18px;line-height:28px}

/* form */
.form-card{left:668px;top:589px;width:465px;height:403px;background:#fff;border-radius:14px;box-shadow:0 6px 24px rgba(0,0,0,.12);padding:52px 20px 0}
.form-card h2{font-size:36px;font-weight:500}
.form-card p{font-size:14px;margin-top:10px;color:#333}
.field{height:41px;border:1px solid #d5d8db;border-radius:3px;font-size:12px;color:#333;display:flex;align-items:center;padding-left:14px}
.row{display:flex;gap:7px;margin-top:25px}
.row .field{flex:1}
.form-card .field.full{margin-top:9px}
.submit{margin-top:12px;height:44px;font-weight:600}

.lead{left:67px;top:768px;width:590px;font-size:46px;line-height:57px}
.tag{left:67px;top:968px;font-size:21px;font-weight:500}
.tag span{color:var(--accent)}

/* feature block */
.grey-panel{left:67px;top:1100px;width:520px;height:497px;background:var(--panel);border-top-right-radius:70px}
.phone{left:165px;top:1145px;width:326px;height:480px;background:#fff;border-radius:12px;box-shadow:0 4px 16px rgba(0,0,0,.15);font-size:10.5px;overflow:hidden}
.phone .hd{display:flex;align-items:center;gap:8px;padding:16px 16px 0;font-weight:600}
.pill{background:#eee;border-radius:8px;padding:2px 7px;font-weight:400;font-size:9px;color:#666}
.times{display:flex;gap:36px;padding:14px 40px 0;font-size:22px;font-weight:600}
.times small{display:block;font-size:10px;font-weight:400;color:#777}
.bubble{position:absolute;border-radius:8px;padding:7px 10px;line-height:13px}
.b-in{background:#f1f1f1}
.b-out{background:#fde5cf}
.msgbox{position:absolute;left:8px;right:8px;bottom:8px;height:64px;background:#f3f3f3;border-radius:8px;padding:10px;color:#666}
.send{position:absolute;right:8px;bottom:8px;background:#111;color:#fff;border-radius:4px;padding:5px 10px;font-weight:600}

.feat{left:637px;width:520px}
.feat .ic{width:54px;height:50px}
.feat h3{font-family:"Inter",sans-serif;font-size:24px;font-weight:500;margin-top:18px}
.feat ul{list-style:none;margin-top:12px;font-size:16.5px;color:#333}
.feat li{margin-bottom:16px}
.feat li::before{content:"▪ ";font-size:12px}

/* conversational section */
.conv{left:0;top:1688px;width:1200px;height:927px;background:var(--teal-dark)}
.conv-kicker{left:0;top:1758px;width:1200px;text-align:center;color:#fff;font-family:"Lexend",sans-serif;font-size:21px}
.conv-title{left:0;top:1780px;width:1200px;text-align:center;color:#fff;font-size:46px}
.card{left:67px;width:560px;border-radius:8px;padding:30px 37px;color:#fff;background:#234b52}
.card.first{background:linear-gradient(180deg,#3e8c90,#2e6d72)}
.card h3{font-size:23px;line-height:29px}
.card ul{list-style:none;margin-top:16px;font-size:14px;line-height:18px}
.card li{margin-bottom:11px;padding-left:11px;position:relative}
.card li::before{content:"";position:absolute;left:0;top:6px;width:5px;height:5px;background:#fff}
.bracket{left:627px;top:1982px;width:40px;height:300px}
.dash{left:693px;top:1888px;width:440px;height:490px;background:#fff;border-radius:60px 0 40px 0;overflow:hidden;font-size:9px;color:#555}
.dash b{color:#111}
.chatov{left:747px;top:2085px;width:206px;height:318px;background:#fff;border-radius:6px;box-shadow:0 4px 16px rgba(0,0,0,.2);font-size:7.5px;color:#333}
.chatov .u{position:absolute;left:30px;width:168px;background:#8a5cf0;color:#fff;border-radius:5px;padding:7px 10px;line-height:10px}
.chatov .a{position:absolute;left:14px;width:170px;background:#f0f0f2;border-radius:5px;padding:7px 14px;line-height:10px}

/* CTA + footer */
.footer-bg{left:0;top:2615px;width:1200px;height:470px;background:var(--footer)}
.cta{left:67px;top:2485px;width:1066px;height:260px;background:#fff;border-radius:130px;text-align:center;padding-top:36px;font-family:"Lexend",sans-serif;font-size:26px;line-height:37px;color:#222}
.cta a{color:#222;font-weight:500;text-decoration:underline}
.cta .btn{width:180px;height:48px;margin:34px auto 0;font-family:"Inter",sans-serif;font-size:15px}
.foot-brand{left:0;top:2785px;width:1200px;justify-content:center;font-size:46px;gap:14px}
.foot-brand .dot{width:74px;height:74px}
.foot-nav{left:0;top:2893px;width:1200px;text-align:center;color:#fff;font-size:12px;word-spacing:3px}
.contact{top:2958px;display:flex;align-items:center;gap:10px;color:#ddd;font-size:16px}
.circ{width:38px;height:38px;border:2px solid var(--teal);border-radius:50%;display:flex;align-items:center;justify-content:center}
.rule{left:187px;top:3020px;width:790px;height:1px;background:#2e3c40}
.copy{left:0;top:3047px;width:1200px;text-align:center;color:#889;font-size:9px}
.copy b{color:#ccc}
.chatbtn{left:975px;top:3002px;width:158px;height:34px;gap:8px;font-size:15px;font-weight:500}
.chatbtn i{width:20px;height:20px;border-radius:50%;background:#fff;display:block}
</style>
</head>
<body>

<div class="abs hero"></div>
<div class="abs brand" style="left:67px;top:12px"><span class="dot"></span>BriskLoom</div>
<nav class="abs nav"><span>Home</span><span>Product</span><span>Platform</span><span>Company</span><span>News</span></nav>
<div class="abs btn" style="left:995px;top:16px;width:138px;height:40px">Contact Us</div>

<div class="abs hero-art" role="img" aria-label="Isometric illustration of a large gear surrounded by four support agents at desks with chat bubbles"></div>
<h1 class="abs hero-title">Meet BriskLoom</h1>
<p class="abs hero-sub">Elevate your users' experience, a new type of conversation awaits.</p>
<div class="abs btn" style="left:671px;top:425px;width:138px;height:38px;font-weight:600">GET STARTED</div>

<form class="abs form-card">
  <h2>Get In Touch</h2>
  <p>Please fill out the form below and our team will be in touch shortly</p>
  <div class="row"><div class="field">First Name</div><div class="field">Last Name</div></div>
  <div class="field full">Work Email Address</div>
  <div class="field full">Phone Number</div>
  <div class="btn submit">SUBMIT</div>
</form>

<h2 class="abs lead">Enhance your customer experience with BriskLoom's AI Assistant.</h2>
<p class="abs tag">Always Ready, <span>Always on - 24/7</span></p>

<div class="abs grey-panel"></div>
<div class="abs phone">
  <div class="hd">← Conference Meeting <span class="pill">4h left</span></div>
  <div class="times"><div>6:00<small>Sat, Dec 11</small></div><div>7:00<small>Sat, Dec 11</small></div></div>
  <div style="position:absolute;left:0;top:95px;width:80px;height:2px;background:#222"></div>
  <div style="position:absolute;top:121px;width:100%;text-align:center;color:#888;font-size:9px">23:40</div>
  <div class="bubble b-in" style="left:30px;top:134px;width:202px">Where do we want to meet guys? I need to know before</div>
  <div class="bubble b-out" style="left:194px;top:184px">Hm ... Let me think</div>
  <div class="bubble b-out" style="left:158px;top:218px;width:150px;height:26px;text-align:right;color:#666">0:30</div>
  <div class="bubble b-in" style="left:30px;top:256px;width:160px;height:112px">What do you want to eat?
    <div style="background:#fff;border-radius:5px;padding:6px 12px;margin-top:10px">Pizza</div>
    <div style="background:#fff;border-radius:5px;padding:6px 12px;margin-top:5px">Burgers</div>
    <div style="font-size:8px;color:#888;margin-top:6px;text-align:center">8 votes · Vote to see results</div></div>
  <div class="msgbox">Message to Conference Meeting</div>
  <div class="send">Send now ⌄</div>
</div>

<div class="abs feat" style="top:1110px">
  <svg class="ic" viewBox="0 0 54 50" fill="none" stroke="#2a6f74" stroke-width="2"><circle cx="38" cy="20" r="11"/><text x="34" y="25" font-size="13" fill="#2a6f74" stroke="none">$</text><path d="M4 20h20M8 14l-5 6 5 6M18 32h20"/></svg>
  <h3>Revolutionize your Customer Interactions</h3>
  <ul><li>Get answers</li><li>Users will find the information they need in seconds</li></ul>
</div>
<div class="abs feat" style="top:1300px">
  <svg class="ic" viewBox="0 0 54 50" fill="none" stroke="#2a6f74" stroke-width="2"><rect x="4" y="14" width="30" height="30" rx="4"/><circle cx="25" cy="32" r="8" fill="#2a8f94" stroke="none"/><path d="M21 32l3 3 5-6" stroke="#fff"/><circle cx="42" cy="10" r="7" fill="#2a8f94" stroke="none"/></svg>
  <h3>Solve Problems</h3>
  <ul><li>Concerns will be addressed quickly with expert assistance</li></ul>
</div>
<div class="abs feat" style="top:1468px">
  <svg class="ic" viewBox="0 0 54 50" fill="none" stroke="#2a6f74" stroke-width="2"><rect x="4" y="4" width="32" height="40" rx="3"/><circle cx="20" cy="26" r="9"/><path d="M14 20l12 12M36 34l14-14"/></svg>
  <h3>Take Action</h3>
  <ul><li>Users will activate services and features immediately</li></ul>
</div>

<div class="abs conv"></div>
<p class="abs conv-kicker">ALL THROUGH NATURAL</p>
<h2 class="abs conv-title">Conversational Experiences</h2>

<div class="abs card first" style="top:1870px;height:160px">
  <h3>BriskLoom enables you to:</h3>
  <ul><li>Engage and delight customers with an AI agent aligned to your brand</li><li>Provide real-time support for a wide variety of uses from simple to complex</li></ul>
</div>
<div class="abs card" style="top:2040px;height:175px">
  <h3>Make AI your own with BriskLoom's conversational platform</h3>
  <ul><li>Ground your BriskLoom AI agent in your company's identity and knowledge</li><li>Solve problems quickly and effectively</li></ul>
</div>
<div class="abs card" style="top:2227px;height:175px">
  <h3>BriskLoom prioritizes trust and security</h3>
  <ul><li>Built-in supervision and auditing</li><li>Secure integrations</li><li>Strong data governance and privacy</li></ul>
</div>
<svg class="abs bracket" viewBox="0 0 40 300" fill="none" stroke="#4f8f95" stroke-width="2"><path d="M0 2c25 0 38 10 38 40v70c0 20 -10 28 -18 36 8 8 18 16 18 36v70c0 30 -13 44 -38 44"/></svg>

<div class="abs dash">
  <div style="position:absolute;left:137px;top:12px;display:flex;gap:6px;align-items:center"><span style="width:14px;height:14px;background:#111;border-radius:3px;display:block"></span><b>Chatvane</b></div>
  <b style="position:absolute;left:398px;top:14px">Studio A</b>
  <div style="position:absolute;left:235px;top:44px;display:flex;gap:18px">Chatbot <span>Settings</span><b style="border-bottom:2px solid #4a5ad8">Dashboard</b><span>Sources</span></div>
  <b style="position:absolute;left:134px;top:74px;font-size:20px">Dashboard</b>
  <div style="position:absolute;left:134px;top:114px;width:96px;height:26px;background:#f2f3f7;border-radius:4px;padding:8px 10px;color:#5a66d8">Chat Logs</div>
  <div style="position:absolute;left:150px;top:152px">Leads</div>
  <div style="position:absolute;left:150px;top:182px">Analytics</div>
  <div style="position:absolute;left:238px;top:114px;width:210px;height:300px;border:1px solid #eee;padding:12px 8px"><b style="font-size:11px">Chat Logs</b>
    <div style="margin-top:14px;background:#f5f5f5;padding:8px;line-height:11px">Hi, what is the delivery time?<br>Depending on the destination, the typical delivery time is 2-5 business days.<br><br>Do you accept payment plans?<br>Unfortunately no! We only accept full payments.</div></div>
</div>
<div class="abs chatov">
  <div style="position:absolute;left:8px;top:10px;display:flex;gap:6px;align-items:center;font-size:10px;font-weight:600"><span style="width:18px;height:18px;border-radius:50%;background:#111;display:block"></span>Studio AI</div>
  <div class="u" style="top:44px">Where can I find examples of previous Work?</div>
  <div class="a" style="top:96px"><u>Here's a link</u> to our portfolio showcasing various projects we've completed.</div>
  <div class="u" style="top:152px">Perfect! I am interested, what are the next steps?</div>
  <div class="a" style="top:210px;height:80px">Please leave your email and we will get back to you shortly.<br><br>Email:<div style="background:#fff;border:1px solid #ddd;height:22px;margin-top:4px"></div></div>
</div>

<div class="abs footer-bg"></div>
<div class="abs cta">
  Discover How BriskLoom can Transform your<br>Customer Experience With Customized Conversational AI.<br><a>Contact Us </a> today to <a>Learn More. </a>
  <div class="btn">LERAN MORE</div>
</div>

<div class="abs brand foot-brand"><span class="dot"></span>BriskLoom</div>
<p class="abs foot-nav">HOME &nbsp;|&nbsp; OUR PRODUCT &nbsp;|&nbsp; PLATFORM &nbsp;|&nbsp; OUR COMPANY &nbsp;|&nbsp; NEWS &nbsp;|&nbsp; CONTACT US</p>
<div class="abs contact" style="left:403px"><span class="circ"><svg width="16" height="16" viewBox="0 0 24 24" fill="#fff"><path d="M6.6 10.8a15 15 0 006.6 6.6l2.2-2.2a1 1 0 011-.3 11 11 0 003.6.6 1 1 0 011 1V20a1 1 0 01-1 1A17 17 0 013 4a1 1 0 011-1h3.5a1 1 0 011 1 11 11 0 00.6 3.6 1 1 0 01-.3 1z"/></svg></span>+2 (555) 014 2290</div>
<div class="abs contact" style="left:619px"><span class="circ"><svg width="16" height="16" viewBox="0 0 24 24" fill="none" stroke="#fff" stroke-width="2"><rect x="3" y="5" width="18" height="14" rx="2"/><path d="M3 7l9 6 9-6"/></svg></span>info@briskloom.example</div>
<div class="abs rule"></div>
<p class="abs copy">© <b>BRISKLOOM</b>, 2024. ALL RIGHTS RESERVED.</p>
<div class="abs btn chatbtn"><i></i>Chat With Us</div>

</body>
</html>
```